Create a bottle Label for Hadstrom American Vodka. LK Hadstrom’ Face (uploaded) should be prominent in the center of the label. The word “Hadstrom” should be above LK’s face and the words “American Vodka” under his face.

Target Market(s)

Buyers of Premium Vodka

Industry/Entity Type

Alcohol

Logo Text

Hadstrom American Vodka

Logo styles of interest
Pictorial/Combination Logo
Character Logo
Colors
00AB8E
00BBA5
67D7C9
C6EFE9
E9F9F6
FFF300
FFF600
FEFA6F
FFFEC7
FFFEE8
FFC000
F8CF3A
FAE287
FDF2CF
FEFAEE
F0912C
F2A743
F7CA91
FBE8D2
FDF5EE
EE7325
F08F49
F5BC92
FAE3D3
FDF4ED

Requirements
Must have
• LK Hadstrom face prominently displayed. The words “Hadstrom”. And “American Vodka”. LK Hadstrom signature.

```html
<!DOCTYPE html>
<html lang="en">
<head>
<meta charset="utf-8">
<title>Hadstrom American Vodka — Label</title>
<link href="https://fonts.googleapis.com/css2?family=Limelight&family=Yellowtail&display=swap" rel="stylesheet">
<style>
  :root {
    --paper: #ffffff;
    --mint-soft: #c6efe9;
    --butter: #fae287;
    --cream: #fffec7;
    --cream-pale: #fffee8;
    --peach: #fbe8d2;
    --rust: #c85a14;
    --orange: #ee7325;
  }
  html, body {
    margin: 0;
    padding: 0;
    width: 960px;
    height: 1200px;
    overflow: hidden;
    background: var(--paper);
  }
  .label {
    display: block;
    width: 960px;
    height: 1200px;
  }
  .label__splash { fill: var(--mint-soft); }
  .label__signature-ground { fill: var(--cream); stroke: var(--cream-pale); stroke-width: 6; }
  .label__signature {
    font-family: "Yellowtail", "Brush Script MT", cursive;
    fill: var(--orange);
    stroke: var(--rust);
    stroke-width: 1.5;
  }
  .label__signature-flourish {
    fill: none;
    stroke: var(--rust);
    stroke-width: 6;
    stroke-linecap: round;
  }
  .label__portrait { fill: url(#portraitTone); }
  .label__star { fill: var(--peach); }
  .label__star--light { fill: var(--paper); }
  .label__plate { fill: var(--butter); }
  .label__plate-inner { fill: var(--cream); }
  .label__wordmark {
    font-family: "Limelight", "Georgia", serif;
    fill: var(--peach);
    stroke: var(--rust);
    stroke-width: 4;
    paint-order: stroke fill;
  }
</style>
</head>
<body>
<svg class="label" viewBox="60 360 640 900" preserveAspectRatio="xMidYMid meet" xmlns="http://www.w3.org/2000/svg">
  <defs>
    <linearGradient id="portraitTone" x1="0" y1="0" x2="1" y2="1">
      <stop offset="0" stop-color="#f08f49"/>
      <stop offset="0.55" stop-color="#ee7325"/>
      <stop offset="1" stop-color="#c85a14"/>
    </linearGradient>
  </defs>

  <path class="label__splash" role="img" aria-label="Soft mint paint splash behind the label"
        d="M110 560 C160 470 300 450 420 470 C520 480 600 520 610 600 C640 700 600 800 650 900
           C680 980 620 1040 640 1120 C650 1200 600 1250 480 1245 C360 1255 220 1250 140 1230
           C90 1180 120 1100 100 1020 C80 940 130 880 110 800 C90 700 80 640 110 560 Z"/>

  <g class="label__signature-block">
    <path class="label__signature-ground"
          d="M100 480 C140 410 250 395 350 400 C440 385 540 395 575 440 C590 480 540 500 470 505
             C360 520 230 560 110 625 C80 640 70 600 90 580 C110 560 95 520 100 480 Z"/>
    <text class="label__signature" x="335" y="485" text-anchor="middle" font-size="92"
          transform="rotate(-8 335 470)">LK Hadstrom</text>
    <path class="label__signature-flourish"
          d="M120 600 C240 540 380 505 560 470"/>
  </g>

  <path class="label__portrait" role="img" aria-label="Portrait of LK Hadstrom in profile, bearded, engraved style"
        d="M190 640 C210 560 300 525 390 530 C470 535 520 590 530 660 C545 700 560 740 555 780
           C570 820 565 870 560 910 C580 935 590 955 585 965 L150 965
           C170 930 200 900 230 880 C200 820 180 730 190 640 Z"/>

  <polygon class="label__star label__star--light" points="140,862 146,878 163,878 149,888 154,904 140,894 126,904 131,888 117,878 134,878"/>
  <polygon class="label__star" points="385,905 392,923 411,923 396,934 402,952 385,941 368,952 374,934 359,923 378,923"/>
  <polygon class="label__star" points="452,895 460,915 481,915 464,927 470,947 452,935 434,947 440,927 423,915 444,915"/>
  <polygon class="label__star" points="533,882 541,903 563,903 545,916 552,937 533,924 514,937 521,916 503,903 525,903"/>

  <rect class="label__plate" x="142" y="955" width="462" height="275" rx="24"/>
  <rect class="label__plate-inner" x="152" y="965" width="442" height="255" rx="18"/>

  <text class="label__wordmark" x="373" y="1055" text-anchor="middle" font-size="96"
        textLength="410" lengthAdjust="spacingAndGlyphs">AMERICAN</text>
  <text class="label__wordmark" x="373" y="1208" text-anchor="middle" font-size="150"
        textLength="410" lengthAdjust="spacingAndGlyphs">VODKA</text>
</svg>
</body>
</html>
```